Packing for Disinfectant wipes

Design the Packinging for new Disinfectant wipes. Wipes are for cleaning and disinfectanting hard surfaces and equipment. There are 100 wipes to the packet (size 230mm x 300mm). The company is called Norbeck Supplies and is supplier of consumable products to healthcare companies. Wipes are not for use on humans/baby. Packaging size as per attachment.
Industry/Entity Type
Healthcare
Requirements
Nice to have
- Packaging need ingredients list and directions for use

```html
<!DOCTYPE html>
<html lang="en">
<head>
<meta charset="utf-8">
<title>Norbeck Supplies – Disinfectant Wipes Pack</title>
<link href="https://fonts.googleapis.com/css2?family=Oswald:wght@500;600&family=Roboto:wght@400;700&display=swap" rel="stylesheet">
<style>
  :root{
    --navy:#2c4a9a;
    --navy-dark:#223c82;
    --sky-light:#e6f6fc;
    --sky:#bfe6f4;
    --sky-deep:#8fcfe8;
    --silver:#c9ced6;
    --white:#ffffff;
    --ink:#1e2430;
    --panel-dark:#2a2f36;
    --bg:#dcdcdc;
  }
  *{margin:0;padding:0;box-sizing:border-box}
  html,body{width:1200px;height:960px;overflow:hidden;background:var(--bg)}
  .pack{position:absolute;left:50px;top:130px;width:1100px;height:700px;font-family:"Roboto",sans-serif}
  .pack-art{position:absolute;inset:0}
  .product-name{position:absolute;left:80px;top:110px;font-family:"Oswald",sans-serif;font-weight:600;font-size:40px;line-height:44px;color:var(--white);letter-spacing:0;white-space:nowrap}
  .germ-free-icon{position:absolute;left:125px;top:235px}
  .brand{position:absolute;left:100px;top:610px;display:flex;align-items:center;gap:10px;color:var(--white);font-size:22px}
  .brand-mark{width:16px;height:16px;background:var(--white)}
  .lid{position:absolute;left:430px;top:70px;width:390px;height:230px;border-radius:34px;background:linear-gradient(160deg,#dff4fb,#a9dcef);box-shadow:0 4px 10px rgba(40,80,120,.2), inset 0 0 0 2px rgba(255,255,255,.6)}
  .claim{position:absolute;left:550px;top:120px;font-family:"Oswald",sans-serif;font-weight:600;font-size:38px;line-height:40px;color:var(--navy);white-space:nowrap}
  .claim-badge{position:absolute;left:470px;top:118px}
  .count{position:absolute;left:925px;top:285px;text-align:center;color:var(--navy);font-family:"Oswald",sans-serif;font-weight:600;font-size:30px;line-height:28px}
  .count small{display:block;font-size:14px;font-weight:500;letter-spacing:1px}
  .count-icon{position:absolute;left:990px;top:288px}
  .surface-icons{position:absolute;left:470px;top:370px;display:flex;gap:22px}
  .first-aid{position:absolute;left:560px;top:455px;width:480px;height:190px;border:2px solid var(--panel-dark);background:var(--white);font-size:8.4px;line-height:11px;color:var(--ink)}
  .first-aid h2{background:var(--panel-dark);color:var(--white);text-align:center;font-size:13px;letter-spacing:1px;padding:3px 0}
  .first-aid p{padding:0 6px;margin-top:3px}
  .first-aid .note{background:var(--panel-dark);color:var(--white);margin-top:6px;padding:3px 6px}
  .maker{position:absolute;left:385px;top:470px;width:160px;font-size:7.5px;line-height:10px;color:var(--ink);text-align:right;font-style:normal}
  .brand-small{position:absolute;left:380px;top:575px;display:flex;align-items:center;gap:6px;color:var(--navy);font-size:15px}
  .brand-small .brand-mark{width:11px;height:11px;background:var(--navy)}
  .instructions{position:absolute;left:380px;top:598px;width:170px;border:2px solid var(--panel-dark);background:var(--white)}
  .instructions h3{background:var(--panel-dark);color:var(--white);font-size:9px;text-align:center;padding:2px 0;letter-spacing:1px}
  .steps{display:flex;gap:3px;padding:4px}
  .step{flex:1;height:38px;background:linear-gradient(#f1f3f5,#dde1e6);border-radius:3px}
</style>
</head>
<body>
<main class="pack">
  <svg class="pack-art" width="1100" height="700" viewBox="0 0 1100 700" aria-hidden="true">
    <defs>
      <linearGradient id="skyFill" x1="0" y1="0" x2="1" y2="1">
        <stop offset="0" stop-color="#eaf8fd"/>
        <stop offset=".5" stop-color="#c6eaf6"/>
        <stop offset="1" stop-color="#9fd6ec"/>
      </linearGradient>
    </defs>
    <rect x="0" y="60" width="60" height="600" fill="var(--navy-dark)"/>
    <rect x="1040" y="40" width="60" height="600" fill="var(--navy-dark)"/>
    <rect x="50" y="20" width="1000" height="660" rx="30" fill="url(#skyFill)"/>
    <path d="M340 440 C430 430 560 420 1050 420 L1050 650 Q1050 680 1020 680 L330 680 Z" fill="var(--white)"/>
    <path d="M80 20 L370 20 C320 180 320 440 345 680 L80 680 Q50 680 50 650 L50 50 Q50 20 80 20 Z" fill="var(--navy)"/>
    <path d="M370 20 C320 180 320 440 345 680" fill="none" stroke="var(--silver)" stroke-width="8"/>
  </svg>

  <h1 class="product-name">DISINFECTANT<br>WIPES</h1>

  <svg class="germ-free-icon" width="110" height="110" viewBox="0 0 110 110" aria-label="No germs icon" role="img">
    <circle cx="55" cy="55" r="48" fill="none" stroke="#fff" stroke-width="6"/>
    <circle cx="55" cy="55" r="16" fill="#fff"/>
    <g stroke="#fff" stroke-width="4" stroke-linecap="round">
      <line x1="55" y1="30" x2="55" y2="22"/><line x1="55" y1="80" x2="55" y2="88"/>
      <line x1="30" y1="55" x2="22" y2="55"/><line x1="80" y1="55" x2="88" y2="55"/>
      <line x1="37" y1="37" x2="31" y2="31"/><line x1="73" y1="73" x2="79" y2="79"/>
      <line x1="73" y1="37" x2="79" y2="31"/><line x1="37" y1="73" x2="31" y2="79"/>
      <line x1="21" y1="89" x2="89" y2="21" stroke-width="6"/>
    </g>
  </svg>

  <div class="brand"><span class="brand-mark"></span>Norbeck Supplies</div>

  <div class="lid"></div>
  <svg class="claim-badge" width="66" height="76" viewBox="0 0 66 76" aria-hidden="true">
    <path d="M33 2 L63 12 L60 44 Q55 64 33 74 Q11 64 6 44 L3 12 Z" fill="#5cb82e" stroke="#9aa3ad" stroke-width="4"/>
  </svg>
  <p class="claim">KILLS 99.9%<br>OF GERMS*</p>

  <p class="count">100<small>WIPES</small></p>
  <svg class="count-icon" width="34" height="34" viewBox="0 0 34 34" aria-label="Not for use on people" role="img">
    <circle cx="17" cy="17" r="14" fill="none" stroke="var(--navy)" stroke-width="2.5"/>
    <line x1="7" y1="27" x2="27" y2="7" stroke="var(--navy)" stroke-width="2.5"/>
  </svg>

  <div class="surface-icons">
    <svg width="56" height="56" viewBox="0 0 56 56" aria-label="Toilet" role="img"><circle cx="28" cy="28" r="25" fill="#fff" stroke="var(--navy)" stroke-width="3"/><rect x="18" y="16" width="8" height="14" fill="var(--navy)"/><path d="M18 30 H40 Q38 40 30 42 V46 H22 V40 Q18 36 18 30 Z" fill="var(--navy)"/></svg>
    <svg width="56" height="56" viewBox="0 0 56 56" aria-label="Washing machine" role="img"><circle cx="28" cy="28" r="25" fill="#fff" stroke="var(--navy)" stroke-width="3"/><rect x="16" y="14" width="24" height="28" rx="2" fill="none" stroke="var(--navy)" stroke-width="3"/><circle cx="28" cy="31" r="7" fill="var(--navy)"/></svg>
    <svg width="56" height="56" viewBox="0 0 56 56" aria-label="Floor tiles" role="img"><circle cx="28" cy="28" r="25" fill="#fff" stroke="var(--navy)" stroke-width="3"/><path d="M16 20 H40 L46 38 H10 Z M22 20 L19 38 M28 20 V38 M34 20 L37 38 M13 29 H43" fill="none" stroke="var(--navy)" stroke-width="2.5"/></svg>
    <svg width="56" height="56" viewBox="0 0 56 56" aria-label="House" role="img"><circle cx="28" cy="28" r="25" fill="#fff" stroke="var(--navy)" stroke-width="3"/><path d="M14 29 L28 16 L42 29 H38 V41 H18 V29 Z" fill="var(--navy)"/><rect x="25" y="32" width="6" height="9" fill="#fff"/></svg>
  </div>

  <section class="first-aid">
    <h2>FIRST AID MEASURES</h2>
    <p><b>Inhalation:</b> Move exposed person to fresh air. Keep warm and at rest. Get medical attention if symptoms occur.</p>
    <p><b>Ingestion:</b> Rinse mouth with water. Do not induce vomiting. Give small amounts of water to drink.</p>
    <p><b>Skin contact:</b> Remove contaminated clothing. Flush skin with plenty of water.</p>
    <p><b>Eye contact:</b> Flush eyes with water for at least 10 minutes. Remove contact lenses.</p>
    <p><b>Protection of first-aiders:</b> No action shall be taken involving any personal risk.</p>
    <p class="note"><b>Notes to physician:</b> Treat symptomatically. Symptoms may be delayed up to 48 hours.</p>
  </section>

  <address class="maker">
    Lindale Care Technology Co., Ltd<br>
    Unit 4, Harbour Industrial Park, Eastvale<br>
    Telephone: +00 555 0142<br>
    Fax: +00 555 0143<br>
    Email: care@lindalecare.example<br>
    <b>Emergency number (24 hours):</b> +00 555 0199
  </address>

  <div class="brand-small"><span class="brand-mark"></span>Norbeck Supplies</div>
  <section class="instructions">
    <h3>INSTRUCTIONS FOR USE</h3>
    <div class="steps">
      <div class="step" role="img" aria-label="Step 1: open the lid"></div>
      <div class="step" role="img" aria-label="Step 2: peel back the seal"></div>
      <div class="step" role="img" aria-label="Step 3: pull out a wipe"></div>
      <div class="step" role="img" aria-label="Step 4: wipe the surface"></div>
      <div class="step" role="img" aria-label="Step 5: close the lid"></div>
    </div>
  </section>
</main>
</body>
</html>
```